Dunmore Acres Enterprise
Home grown grain fed beef Wholes, Halfs, Quarters
Locally raised
No Added Hormones
Call or text now to order (555) -0418-2957

```html
<!DOCTYPE html>
<html lang="en">
<head>
<meta charset="utf-8">
<title>Dunmore Acres Enterprise – Home Grown Grain Fed Beef</title>
<link rel="stylesheet" href="https://fonts.googleapis.com/css2?family=Bebas+Neue&family=League+Spartan:wght@700;800&display=swap">
<style>
  :root {
    --bg: #2e2215;
    --bg-deep: #261b10;
    --cream: #f2e9a6;
    --white: #ffffff;
    --ink: #2b1e12;
    --green: #22d60f;
    --hide-tan: #a86a3c;
    --hide-dark: #3a2818;
    --hide-light: #c99a72;
  }
  * { margin: 0; padding: 0; box-sizing: border-box; }
  html, body { width: 1200px; height: 846px; overflow: hidden; background: var(--bg); }
  .flyer {
    position: relative;
    width: 1200px;
    height: 846px;
    overflow: hidden;
    background: radial-gradient(ellipse at 30% 30%, #3a2c1c 0%, var(--bg) 55%, var(--bg-deep) 100%);
    font-family: "League Spartan", sans-serif;
  }
  .herd-photo {
    position: absolute;
    left: 520px;
    top: 0;
    width: 680px;
    height: 846px;
    background:
      radial-gradient(ellipse 180px 240px at 460px 340px, var(--hide-light) 0%, transparent 70%),
      radial-gradient(ellipse 260px 380px at 470px 420px, var(--hide-tan) 0%, transparent 75%),
      radial-gradient(ellipse 220px 320px at 290px 650px, var(--hide-tan) 0%, transparent 75%),
      radial-gradient(ellipse 160px 200px at 330px 720px, var(--hide-dark) 0%, transparent 80%),
      linear-gradient(180deg, #4a3624 0%, #5a4029 50%, #3a2a1b 100%);
    -webkit-mask-image: linear-gradient(90deg, transparent 0%, #000 40%);
    mask-image: linear-gradient(90deg, transparent 0%, #000 40%);
  }
  .brand-name {
    position: absolute;
    left: 56px;
    top: 78px;
    color: var(--cream);
    font-weight: 800;
    font-size: 81px;
    line-height: 80px;
    letter-spacing: 1px;
    text-transform: uppercase;
  }
  .tagline {
    position: absolute;
    left: 59px;
    top: 346px;
    color: var(--white);
    font-weight: 700;
    font-size: 44px;
    letter-spacing: 0.5px;
  }
  .cuts {
    position: absolute;
    left: 56px;
    top: 422px;
    display: flex;
    gap: 16px;
    list-style: none;
  }
  .cut {
    width: 192px;
    height: 78px;
    background: var(--white);
    padding: 5px;
  }
  .cut span {
    display: flex;
    align-items: center;
    justify-content: center;
    width: 100%;
    height: 100%;
    border: 2px solid var(--ink);
    color: var(--ink);
    font-family: "Bebas Neue", sans-serif;
    font-size: 54px;
    line-height: 1;
    padding-top: 5px;
  }
  .benefits {
    position: absolute;
    left: 58px;
    top: 566px;
    list-style: none;
  }
  .benefit {
    display: flex;
    align-items: center;
    height: 60px;
    color: var(--green);
    font-weight: 700;
    font-size: 40px;
  }
  .benefit svg { width: 40px; height: 36px; margin-right: 8px; flex: none; margin-top: -6px; }
  .cta {
    position: absolute;
    left: 54px;
    top: 732px;
    color: var(--white);
    font-family: "Bebas Neue", sans-serif;
    font-size: 48px;
    line-height: 1;
  }
  .cta .phone { color: var(--green); }
</style>
</head>
<body>
<main class="flyer">
  <div class="herd-photo" role="img" aria-label="Photo of two brown cattle with ear tags looking out from a barn stall"></div>

  <h1 class="brand-name">Dunmore Acres<br>Enterprise</h1>

  <p class="tagline">Home Grown Grain Fed Beef</p>

  <ul class="cuts">
    <li class="cut"><span>Wholes</span></li>
    <li class="cut"><span>Halfs</span></li>
    <li class="cut"><span>Quarters</span></li>
  </ul>

  <ul class="benefits">
    <li class="benefit">
      <svg viewBox="0 0 40 36" aria-hidden="true"><path d="M2 20 L8 14 L15 22 L33 2 L39 8 L15 34 Z" fill="var(--green)"/></svg>
      Locally Raised
    </li>
    <li class="benefit">
      <svg viewBox="0 0 40 36" aria-hidden="true"><path d="M2 20 L8 14 L15 22 L33 2 L39 8 L15 34 Z" fill="var(--green)"/></svg>
      No Added Hormones
    </li>
  </ul>

  <p class="cta">Call or text now to order <span class="phone">(555) -0418-2957</span></p>
</main>
</body>
</html>
```